College Advising Business Card Design

We need a business card design for a new company. We advise students and their families on finding the right colleges to apply to; the application process; creating resumes; writing essays; and once students are accepted, figuring out what the best fit is. We pride ourselves on highly personal service, and we travel the country to learn about schools. The visual we have used on our website is a picture of a graduation caps tossed into the blue sky. See my website.

Target Market(s)

Parents of high school students

Industry/Entity Type

Travel

Contact Information for Business Card

COLLEGE IS THE DREAM. LET US HELP YOU FIND THE DESTINATION.

Marta Delvecchi Ornbrook and Associates
College Admissions Advising and Essay Guidance
enroll@martadelvecchiornbrook.example
555-418-PATH (7284)
Follow us on Friendspace

```html
<!DOCTYPE html>
<html lang="en">
<head>
<meta charset="utf-8">
<title>Marta Delvecchi Ornbrook and Associates – Business Card</title>
<link href="https://fonts.googleapis.com/css2?family=Cinzel:wght@700&family=Arimo:wght@400&display=swap" rel="stylesheet">
<style>
  :root {
    --page-bg: #f4f4f4;
    --card-white: #ffffff;
    --sky-deep: #2f8fd0;
    --sky-light: #8cc6ee;
    --band-blue: #3592d2;
    --ink: #1b1b1b;
    --brick: #a3391f;
  }
  html, body {
    margin: 0;
    width: 1200px;
    height: 821px;
    overflow: hidden;
    background: var(--page-bg);
  }
  .business-card {
    position: absolute;
    left: 100px;
    top: 125px;
    width: 1000px;
    height: 572px;
    background: var(--card-white);
    box-shadow: 0 6px 24px rgba(0,0,0,0.15);
    overflow: hidden;
    font-family: "Arimo", Arial, sans-serif;
    color: var(--ink);
  }
  .sky-photo {
    position: absolute;
    left: 0; top: 0;
    width: 100%;
    height: 190px;
    background: linear-gradient(180deg, var(--sky-deep) 0%, var(--sky-light) 100%);
  }
  .side-stripe {
    position: absolute;
    top: 330px;
    height: 34px;
    background: var(--band-blue);
  }
  .side-stripe--left { left: 0; width: 120px; }
  .side-stripe--right { right: 0; width: 190px; }
  .tagline {
    position: absolute;
    left: 0; right: 0;
    top: 200px;
    margin: 0;
    text-align: center;
    font-family: "Cinzel", "Times New Roman", serif;
    font-weight: 700;
    font-size: 36px;
    line-height: 40px;
    letter-spacing: 1px;
    text-transform: uppercase;
  }
  .contact-block {
    position: absolute;
    left: 0; right: 0;
    top: 292px;
    text-align: center;
  }
  .firm-name {
    margin: 0;
    color: var(--brick);
    font-size: 24px;
    letter-spacing: 1.5px;
    text-transform: uppercase;
  }
  .services {
    display: inline-block;
    margin: 10px 0 0;
    padding-bottom: 6px;
    font-size: 19px;
    border-bottom: 3px solid var(--band-blue);
  }
  .email, .phone {
    margin: 10px 0 0;
    font-size: 19px;
  }
  .phone { font-size: 24px; letter-spacing: 1px; }
  .social-band {
    position: absolute;
    left: 0; right: 0;
    top: 462px;
    height: 46px;
    background: var(--band-blue);
    display: flex;
    align-items: center;
    justify-content: center;
  }
  .social-band p {
    margin: 0;
    color: var(--brick);
    font-size: 19px;
  }
</style>
</head>
<body>
  <div class="business-card">
    <div class="sky-photo" role="img" aria-label="Graduation caps tossed into a blue sky with white clouds"></div>
    <div class="side-stripe side-stripe--left"></div>
    <div class="side-stripe side-stripe--right"></div>
    <h1 class="tagline">College is the dream.<br>Let us help you find the destination.</h1>
    <div class="contact-block">
      <p class="firm-name">Marta Delvecchi Ornbrook &amp; Associates College</p>
      <p class="services">Admissions Advising and Essay Guidance</p>
      <p class="email">enroll@martadelvecchiornbrook.example</p>
      <p class="phone">555-418-PATH (7284)</p>
    </div>
    <div class="social-band">
      <p>Follow us on Friendspace</p>
    </div>
  </div>
</body>
</html>
```